Dampfbadtechnik und Ausstattung Produktübersicht 2016/2017
lumavo suchte ein neues Design in der Kategorie Broschüre und hat ein Projekt auf entwurfmarkt.de gestartet.
Zielgruppe
Wir verkaufen die Technik sowie generell die Austattung für Dampfbäder. Sanitärbetriebe, Private Kunden die selbst ein Dampfbad bauen, Fliesenfachbetriebe, Wellnesscenter..
Aufgabenstellung
Alles möglich (Format, Design,..). Es handelt sich um eine Produktübersicht unserer Produkte. Unsere Kunden sind Sanitärbetriebe, Private Kunden die selbst ein Dampfbad bauen, Fliesenfachbetriebe, Wellnesscenter..
Fotos und Texte die Sie für den Folder Verwenden können finden Sie unter:
www.nebelraumwerk.com bzw. www.hitzequelle-vorta.at/de/Referenzen.html
Ich würde gerne Broschüren drucken und den Kunden zusenden.

```html
<!DOCTYPE html>
<html lang="de">
<head>
<meta charset="utf-8">
<title>Nebelreich – Dampfbadtechnik und Ausstattung</title>
<link rel="stylesheet" href="https://fonts.googleapis.com/css2?family=Poiret+One&display=swap">
<style>
  :root {
    --navy: #1b3f78;
    --cyan: #00b2e3;
    --paper: #ffffff;
    --tile-deep: #1d4f8f;
    --tile-mid: #2f7fc4;
    --tile-light: #4fb6ea;
  }
  html, body {
    margin: 0;
    padding: 0;
    overflow: hidden;
    background: var(--paper);
  }
  .brochure-cover {
    position: relative;
    width: 1200px;
    height: 846px;
    background: var(--paper);
    overflow: hidden;
    font-family: "Poiret One", sans-serif;
    color: var(--navy);
  }
  .hero-rule {
    position: absolute;
    left: 0;
    width: 1200px;
    height: 4px;
    background: var(--cyan);
  }
  .hero-rule--top { top: 159px; }
  .hero-rule--bottom { top: 549px; }
  .hero-photo {
    position: absolute;
    left: 0;
    top: 163px;
    width: 1200px;
    height: 386px;
    background:
      linear-gradient(100deg, rgba(29,79,143,0.85) 0%, rgba(29,79,143,0.2) 40%, rgba(79,182,234,0.1) 60%, rgba(79,182,234,0.9) 100%),
      linear-gradient(180deg, var(--tile-mid) 0%, var(--tile-deep) 55%, var(--tile-light) 100%);
  }
  .brand-panel {
    position: absolute;
    left: 56px;
    top: 120px;
    width: 356px;
    height: 111px;
    background: var(--paper);
  }
  .brand-rule {
    position: absolute;
    left: 27px;
    top: 11px;
    width: 306px;
    height: 2px;
    background: var(--cyan);
  }
  .brand-name {
    position: absolute;
    left: 27px;
    top: 24px;
    margin: 0;
    font-size: 50px;
    line-height: 1;
    font-weight: 400;
    color: var(--navy);
    letter-spacing: 1px;
  }
  .brand-tagline {
    position: absolute;
    left: 28px;
    top: 82px;
    margin: 0;
    font-size: 13.5px;
    font-weight: 400;
    letter-spacing: 0.6px;
    color: var(--navy);
  }
  .cover-title {
    position: absolute;
    right: 172px;
    margin: 0;
    font-weight: 400;
    font-size: 39px;
    line-height: 1;
    letter-spacing: 2px;
    color: var(--navy);
    white-space: nowrap;
  }
  .cover-title--main { top: 596px; }
  .cover-title--sub { top: 652px; }
  .title-rule {
    position: absolute;
    left: 0;
    top: 639px;
    width: 1028px;
    height: 4px;
    background: var(--cyan);
  }
</style>
</head>
<body>
  <main class="brochure-cover">
    <div class="hero-rule hero-rule--top"></div>
    <div class="hero-photo" role="img" aria-label="Dampfbad mit blauem Glasmosaik, Liegebank und weißem Waschbecken"></div>
    <div class="hero-rule hero-rule--bottom"></div>

    <div class="brand-panel">
      <div class="brand-rule"></div>
      <p class="brand-name">Nebelreich</p>
      <p class="brand-tagline">SOLE UND DAMPFBADTECHNIK</p>
    </div>

    <h1 class="cover-title cover-title--main">Dampfbadtechnik und Ausstattung</h1>
    <div class="title-rule"></div>
    <h2 class="cover-title cover-title--sub">Produktübersicht 2016/2017</h2>
  </main>
</body>
</html>
```